Weddings by Marla

Nice ad or card design to advertise my hair business. I like to accentuate 'Marla'

some of the things on my card/ad now are:

Full service hair artist
Available for your special occasion

up-do's for you or your sheitle
Temporary hair extensions, cuts, color, Hi-lites, perms, and waxing

phone, emial, website
Updates

Project Deadline Extended
Reason: I chose a design but it needed a minor change but i have not heard back from the designer. I am still hoping to finalize that design. thank you

Target Market(s)

women all ages

Industry/Entity Type

Hair

```html
<!DOCTYPE html>
<html lang="en">
<head>
<meta charset="utf-8">
<title>Marla – hair artist</title>
<link rel="stylesheet" href="https://fonts.googleapis.com/css2?family=Lobster&family=Fondamento&display=swap">
<style>
  :root {
    --blush: #f2a9a6;
    --blush-light: #f6c0bd;
    --swirl: #fbdcda;
    --title-orange: #e58148;
    --title-outline: #6b3420;
    --brown: #7a3b22;
    --ink: #231614;
  }
  html, body {
    margin: 0;
    padding: 0;
    overflow: hidden;
    background: #ffffff;
  }
  .card {
    position: relative;
    width: 686px;
    height: 1200px;
    overflow: hidden;
    background: var(--blush);
    font-family: "Fondamento", serif;
  }
  .flourish {
    position: absolute;
    left: 0;
    top: 0;
    width: 686px;
    height: 1200px;
    background:
      radial-gradient(ellipse 260px 520px at 120px 560px, rgba(251,220,218,0.55), rgba(251,220,218,0) 70%),
      radial-gradient(ellipse 260px 200px at 520px 70px, rgba(251,220,218,0.5), rgba(251,220,218,0) 70%);
  }
  .services-band {
    position: absolute;
    left: 0;
    top: 545px;
    width: 686px;
    height: 245px;
    background: var(--blush-light);
    opacity: 0.8;
  }
  .brand-name {
    position: absolute;
    left: 0;
    top: 95px;
    width: 686px;
    margin: 0;
    text-align: center;
    font-family: "Lobster", cursive;
    font-weight: 400;
    font-size: 170px;
    line-height: 1;
    color: var(--title-orange);
    -webkit-text-stroke: 3px var(--title-outline);
  }
  .tagline {
    position: absolute;
    left: 0;
    top: 262px;
    width: 760px;
    margin: 0;
    text-align: center;
    font-family: "Fondamento", serif;
    font-size: 46px;
    color: var(--brown);
    letter-spacing: 1px;
  }
  .services {
    position: absolute;
    left: 38px;
    top: 580px;
    margin: 0;
    padding: 0;
    list-style: none;
    font-size: 30px;
    line-height: 40px;
    color: var(--ink);
  }
  .contact {
    position: absolute;
    left: 150px;
    top: 980px;
    margin: 0;
    padding: 0;
    list-style: none;
    color: var(--ink);
    font-size: 32px;
  }
  .contact li {
    display: flex;
    align-items: center;
    height: 56px;
  }
  .contact svg {
    width: 40px;
    height: 40px;
    margin-right: 18px;
    flex: none;
  }
  .contact .email { font-size: 27px; font-style: italic; }
  .contact .social { font-size: 30px; }
</style>
</head>
<body>
  <div class="card">
    <div class="flourish" role="img" aria-label="Soft white swirling vine flourish with leaves"></div>
    <div class="services-band"></div>

    <h1 class="brand-name">Marla</h1>
    <p class="tagline">hair artist</p>

    <ul class="services">
      <li>- Available for your special occasion.</li>
      <li>- Up-do's for you or your sheitle.</li>
      <li>- Temporary hair extensions.</li>
      <li>- Cuts, color, Hi-lites, perms, and waxing.</li>
    </ul>

    <ul class="contact">
      <li class="phone">
        <svg viewBox="0 0 40 40" aria-hidden="true">
          <circle cx="20" cy="20" r="17" fill="none" stroke="#231614" stroke-width="3"/>
          <path d="M14 11c2-1 3 0 4 3l-2 2c1 3 3 5 6 6l2-2c3 1 4 2 3 4-1 2-3 3-5 2-6-2-10-6-11-11 0-2 1-3 3-4z" fill="#231614"/>
        </svg>
        410.555.0148
      </li>
      <li class="email">
        <svg viewBox="0 0 40 40" aria-hidden="true">
          <rect x="3" y="9" width="34" height="23" fill="#231614"/>
          <path d="M3 9l17 13 17-13" fill="none" stroke="#f2a9a6" stroke-width="2.5"/>
        </svg>
        marlastyles@example.net
      </li>
      <li class="social">
        <svg viewBox="0 0 40 40" aria-hidden="true">
          <rect x="8" y="6" width="26" height="28" fill="#231614"/>
        </svg>
        Social.com/ marlastyles
      </li>
    </ul>
  </div>
</body>
</html>
```